Business Card design for construction company

I would like a business card design for a construction company - Harlow Constructions. I have attached the ai logo file for use. I would like the card to be very smart and clean and incorporate only white and the two colours in the logo. I would like the card to have two sides. One side can just have the logo, the other with the relevant information.

Target Market(s)

Building and Construction Clients

Industry/Entity Type

Business

Contact Information for Business Card

Name: Tom Pardoe
Company: Harlow Constructions Pty Limited
Address: 14 Mallee Crescent Carrow Vale 2093
Phone: 0427 531 068
Email: tomp@harlowbuild-example.com.au

Font styles to use
Serif
Sans Serif

Requirements
Must have
• Details noted above
• Logo as provided
• Colours as in logo
• Square edges
• A font that compliments the logo
Should not have
• Any colour other than white and those in logo
• Rounded edges

```html
<!DOCTYPE html>
<html lang="en">
<head>
<meta charset="utf-8">
<title>Harlow Constructions – Business Card</title>
<link rel="stylesheet" href="https://fonts.googleapis.com/css2?family=Lato:wght@400&display=swap">
<style>
  :root {
    --page: #e8ecef;
    --card: #ffffff;
    --ink: #6d6e70;
    --accent: #00aee6;
  }
  html, body {
    margin: 0;
    padding: 0;
    width: 1200px;
    height: 1200px;
    overflow: hidden;
    background: var(--page);
    font-family: "Lato", sans-serif;
  }
  .sheet {
    position: relative;
    width: 1200px;
    height: 1200px;
  }
  .card {
    position: absolute;
    left: 309px;
    width: 553px;
    height: 307px;
    background: var(--card);
    color: var(--ink);
    overflow: hidden;
  }
  .card--front { top: 254px; }
  .card--back  { top: 638px; }

  .brand-name {
    position: absolute;
    margin: 0;
    font-weight: 400;
    font-size: 20px;
    line-height: 24px;
    letter-spacing: 0.15em;
    text-transform: uppercase;
    color: var(--ink);
    white-space: nowrap;
  }
  .card--front .brand-name {
    left: 0;
    right: 0;
    top: 140px;
    text-align: center;
  }
  .address {
    position: absolute;
    left: 0;
    right: 0;
    top: 254px;
    margin: 0;
    text-align: center;
    font-size: 18px;
    color: var(--ink);
  }

  .back-rule {
    position: absolute;
    left: 159px;
    width: 3px;
    background: var(--accent);
  }
  .back-rule--upper { top: 12px; height: 180px; }
  .back-rule--lower { top: 257px; height: 33px; }

  .brand-square {
    position: absolute;
    left: 124px;
    top: 143px;
    width: 12px;
    height: 12px;
    background: var(--accent);
  }
  .card--back .brand-name {
    left: 184px;
    top: 137px;
  }

  .contact-list {
    position: absolute;
    left: 152px;
    top: 194px;
    margin: 0;
    padding: 0;
    list-style: none;
  }
  .contact-list li {
    display: flex;
    align-items: center;
    height: 20px;
    font-size: 14px;
    color: var(--ink);
  }
  .contact-icon {
    width: 18px;
    height: 14px;
    margin-right: 18px;
    fill: var(--accent);
    flex: none;
  }
</style>
</head>
<body>
<main class="sheet">

  <section class="card card--front" aria-label="Card front">
    <h1 class="brand-name">Harlow Constructions</h1>
    <p class="address">14 Mallee Crescent, Carrow Vale, 2093</p>
  </section>

  <section class="card card--back" aria-label="Card back">
    <div class="back-rule back-rule--upper"></div>
    <div class="brand-square"></div>
    <h2 class="brand-name">Harlow Constructions</h2>

    <ul class="contact-list">
      <li>
        <svg class="contact-icon" viewBox="0 0 18 14" aria-hidden="true">
          <circle cx="9" cy="3.5" r="3"/>
          <path d="M4 14 C4 9 6 7.5 9 7.5 C12 7.5 14 9 14 14 Z"/>
        </svg>
        Tom Pardoe
      </li>
      <li>
        <svg class="contact-icon" viewBox="0 0 18 14" aria-hidden="true">
          <text x="9" y="12" text-anchor="middle" font-size="13" font-family="Lato, sans-serif">@</text>
        </svg>
        tomp@harlowbuild-example.com.au
      </li>
      <li>
        <svg class="contact-icon" viewBox="0 0 18 14" aria-hidden="true">
          <path d="M5.5 1.5 L7.5 1 L8.5 4 L7 5.2 C7.6 6.8 8.8 8 10.4 8.7 L11.6 7.2 L14.5 8.3 L14 10.4 C13.6 11.6 12.6 12 11.5 11.8 C7.5 11 4.6 8 4 4 C3.8 2.8 4.3 1.9 5.5 1.5 Z"/>
        </svg>
        0427531068
      </li>
    </ul>

    <div class="back-rule back-rule--lower"></div>
  </section>

</main>
</body>
</html>
```